Design some Business Cards for Paw Haven

Hi There,

After some business cards for a business that does dog walking, at home pet visits and pet day care.

Attached is the logo in both PNG and PSD format. Design should be simple and clean, with a white background both on the front and the back. Logo should be on the front and the following on the back:

Mara Fenwick
Dog Walking At Home Pet Visits Pet Day Care
0411375926

Looking forward to your designs!
Thanks

```html
<!DOCTYPE html>
<html lang="en">
<head>
<meta charset="utf-8">
<title>Paw Haven – Business Cards</title>
<link rel="stylesheet" href="https://fonts.googleapis.com/css2?family=Comfortaa:wght@400;700&display=swap">
<style>
  :root {
    --backdrop: #eceef2;
    --card: #ffffff;
    --blue-deep: #4a5cc4;
    --blue-mid: #7e8ad6;
    --blue-pale: #dfe3f6;
    --ink: #1c2340;
    --name-blue: #3b50c2;
    --white: #ffffff;
  }
  * { margin: 0; padding: 0; box-sizing: border-box; }
  html, body {
    width: 1200px; height: 899px; overflow: hidden;
    background: var(--backdrop);
    font-family: "Comfortaa", sans-serif;
  }
  .stage { position: relative; width: 1200px; height: 899px; }
  .card {
    position: absolute; left: 325px; width: 550px; height: 307px;
    background: var(--card); overflow: hidden;
    box-shadow: 0 2px 8px rgba(28,35,64,.18);
  }
  .card--front { top: 110px; }
  .card--back { top: 470px; }
  .card__waves { position: absolute; inset: 0; width: 100%; height: 100%; }

  .brand { position: absolute; left: 0; right: 0; top: 62px; text-align: center; }
  .brand__dot {
    display: block; margin: 0 auto 26px; width: 92px; height: 92px;
    border-radius: 50%; background: var(--ink);
  }
  .brand__name { font-size: 42px; font-weight: 400; color: var(--ink); letter-spacing: .5px; }

  .owner { position: absolute; left: 38px; top: 22px; }
  .owner__name { font-size: 40px; font-weight: 700; color: var(--name-blue); line-height: 1; }
  .owner__brand { margin: 4px 0 0 120px; font-size: 11px; color: var(--ink); }

  .services { position: absolute; left: 152px; top: 112px; width: 275px; list-style: none; }
  .services__item {
    height: 27px; margin-bottom: 13px; text-align: center;
    line-height: 27px; font-size: 17px; font-weight: 700; color: var(--white);
    background: linear-gradient(180deg, var(--blue-mid) 0%, var(--blue-deep) 50%, var(--blue-mid) 100%);
    border: 1px solid var(--blue-pale);
  }
  .services__post {
    position: absolute; top: -14px; width: 4px; height: 44px; background: var(--ink);
  }
  .services__post--left { left: -6px; }
  .services__post--right { right: -6px; }

  .phone {
    position: absolute; left: 336px; top: 241px; width: 134px; height: 32px;
    line-height: 32px; text-align: center; font-size: 17px; font-weight: 700;
    color: var(--white); background: var(--blue-deep); border: 2px solid var(--blue-pale);
  }
  .mini-brand { position: absolute; left: 480px; top: 244px; width: 60px; text-align: center; }
  .mini-brand__dot { display: block; margin: 0 auto 3px; width: 16px; height: 16px; border-radius: 50%; background: var(--ink); }
  .mini-brand__name { font-size: 8px; color: var(--ink); }
</style>
</head>
<body>
<main class="stage">

  <section class="card card--front" aria-label="Business card front">
    <svg class="card__waves" viewBox="0 0 550 307" preserveAspectRatio="none" aria-hidden="true">
      <defs>
        <linearGradient id="bandTop" x1="0" y1="0" x2="0" y2="1">
          <stop offset="0" stop-color="#4a5cc4"/><stop offset="1" stop-color="#dfe3f6"/>
        </linearGradient>
        <linearGradient id="bandBottom" x1="0" y1="1" x2="0" y2="0">
          <stop offset="0" stop-color="#4a5cc4"/><stop offset="1" stop-color="#ffffff"/>
        </linearGradient>
      </defs>
      <path d="M0 0 H550 V18 C420 32 300 6 150 20 C90 26 40 22 0 18 Z" fill="url(#bandTop)"/>
      <path d="M0 307 H550 V238 C470 258 380 300 250 272 C150 250 70 262 0 282 Z" fill="url(#bandBottom)"/>
    </svg>
    <div class="brand">
      <span class="brand__dot"></span>
      <span class="brand__name">Paw Haven</span>
    </div>
  </section>

  <section class="card card--back" aria-label="Business card back">
    <svg class="card__waves" viewBox="0 0 550 307" preserveAspectRatio="none" aria-hidden="true">
      <defs>
        <linearGradient id="bandTopB" x1="0" y1="0" x2="0" y2="1">
          <stop offset="0" stop-color="#4a5cc4"/><stop offset="1" stop-color="#ffffff"/>
        </linearGradient>
        <linearGradient id="bandBottomB" x1="0" y1="1" x2="0" y2="0">
          <stop offset="0" stop-color="#4a5cc4"/><stop offset="1" stop-color="#ffffff"/>
        </linearGradient>
      </defs>
      <path d="M0 0 H550 V44 C470 20 380 14 300 30 C220 46 120 40 0 20 Z" fill="url(#bandTopB)"/>
      <path d="M0 307 H550 V250 C460 270 360 282 260 262 C160 244 80 250 0 262 Z" fill="url(#bandBottomB)"/>
    </svg>

    <header class="owner">
      <h1 class="owner__name">Mara Fenwick</h1>
      <p class="owner__brand">Paw Haven</p>
    </header>

    <ul class="services">
      <span class="services__post services__post--left" aria-hidden="true"></span>
      <span class="services__post services__post--right" aria-hidden="true"></span>
      <li class="services__item">At Home Pet Visits</li>
      <li class="services__item">Pet Day Care</li>
      <li class="services__item">Dog Walking</li>
    </ul>

    <p class="phone">0411375926</p>
    <div class="mini-brand">
      <span class="mini-brand__dot"></span>
      <span class="mini-brand__name">Paw Haven</span>
    </div>
  </section>

</main>
</body>
</html>
```